Company identity deisgn should support 2 languages

I would like to get our company identity design
This includes the following only
Business Cards 2 languages Arabic and English
Email signature
Letterhead
Linkedin profile images
Attached is the logo in Ai format

Requirements
Must have
• For business card
Must have
Name and Adrees in arabic
Name and Address in english
You might use both side of the card
Should not have
• Any pictures other than the logo

```html
<!DOCTYPE html>
<html lang="en">
<head>
<meta charset="utf-8">
<title>Northwind Cognition Letterhead</title>
<link href="https://fonts.googleapis.com/css2?family=Open+Sans:wght@400&family=Roboto:wght@300;400&family=Noto+Sans+Arabic:wght@400&display=swap" rel="stylesheet">
<style>
  :root {
    --backdrop: #dedede;
    --sheet-tint: #f7f7f7;
    --sheet-white: #ffffff;
    --brand-blue: #1f77c0;
    --ink: #4a4a4a;
    --ink-soft: #5a5a5a;
    --signature-fill: #ececec;
  }
  * { margin: 0; padding: 0; box-sizing: border-box; }
  html, body {
    width: 1200px; height: 800px; overflow: hidden;
    background: var(--backdrop);
  }
  .stage { position: relative; width: 1200px; height: 800px; }
  .letterhead {
    position: absolute; top: 111px;
    width: 412px; height: 574px;
  }
  .letterhead--tinted { left: 165px; background: var(--sheet-tint); }
  .letterhead--white { left: 613px; background: var(--sheet-white); }

  .brand {
    position: absolute; left: 37px; top: 47px;
    display: flex; align-items: center; gap: 6px;
    font-family: "Roboto", sans-serif; font-weight: 400;
    font-size: 10px; letter-spacing: 0.6px;
    color: var(--brand-blue);
  }
  .brand-dot {
    width: 16px; height: 16px; border-radius: 50%;
    background: var(--brand-blue);
  }

  .contact-list {
    position: absolute; right: 37px; top: 40px;
    list-style: none;
    font-family: "Roboto", sans-serif; font-weight: 300;
    font-size: 9.6px; line-height: 11.3px; color: var(--ink);
  }
  .contact-list li { display: flex; align-items: center; gap: 3px; }
  .contact-icon { width: 8px; height: 8px; fill: var(--brand-blue); flex: none; }

  .letter-body {
    position: absolute; left: 37px; top: 139px; width: 338px;
    font-family: "Open Sans", sans-serif; font-size: 7.6px;
    line-height: 11.1px; color: var(--ink);
  }
  .salutation { margin-bottom: 11px; }
  .letter-body p.paragraph { text-align: justify; margin-bottom: 11px; }
  .closing { position: absolute; left: 37px; top: 372px;
    font-family: "Open Sans", sans-serif; font-size: 7.6px; color: var(--ink); }
  .signature-area {
    position: absolute; left: 37px; top: 398px;
    width: 50px; height: 46px; background: var(--signature-fill);
  }

  .address {
    position: absolute; top: 530px;
    font-family: "Roboto", sans-serif; font-weight: 300;
    font-size: 9.4px; line-height: 11.3px; color: var(--ink-soft);
  }
  .address--en { left: 37px; }
  .address--ar {
    right: 37px; top: 526px; text-align: right; direction: rtl;
    font-family: "Noto Sans Arabic", sans-serif; font-size: 8.6px; line-height: 12.4px;
  }
</style>
</head>
<body>
<div class="stage">

  <article class="letterhead letterhead--tinted">
    <div class="brand"><span class="brand-dot"></span>NORTHWIND COGNITION</div>
    <ul class="contact-list">
      <li><svg class="contact-icon" viewBox="0 0 10 10"><path d="M1 4c0-2 2-3 4-3s4 1 4 3H7V3H3v1zM2 5h6l1 4H1z"/></svg>555.204.7781</li>
      <li><svg class="contact-icon" viewBox="0 0 10 10"><path d="M0 2h10v6H0z M0 2l5 3.5L10 2" stroke="#fff" stroke-width="0.8"/></svg>hello@northwindmail.com</li>
      <li><svg class="contact-icon" viewBox="0 0 10 10"><circle cx="5" cy="5" r="4.6"/><path d="M3 2.5l2 1-1 2 2 1-1 2M7 2l1 2" stroke="#fff" stroke-width="0.7" fill="none"/></svg>www.northwindweb.com</li>
    </ul>
    <div class="letter-body">
      <p class="salutation">Dear customer,</p>
      <p class="paragraph">Lorem ipsum dolor sit amet, consectetur adipisicing elit, sed do eiusmod tempor incididunt ut labore et dolore magna aliqua. Ut enim ad minim veniam, quis nostrud exercitation ullamco laboris nisi ut aliquip ex ea commodo consequat. Duis aute irure dolor in reprehenderit in voluptate velit esse cillum dolore eu fugiat nulla pariatur. Excepteur sint occaecat cupidatat non proident, sunt in culpa qui officia deserunt mollit anim id est laborum.</p>
      <p class="paragraph">Lorem ipsum dolor sit amet, consectetur adipisicing elit, sed do eiusmod tempor incididunt ut labore et dolore magna aliqua. Ut enim ad minim veniam, quis nostrud exercitation ullamco laboris nisi ut aliquip ex ea commodo consequat. Duis aute irure dolor in reprehenderit in voluptate velit esse cillum dolore eu fugiat nulla pariatur. Excepteur sint occaecat cupidatat non proident, sunt in culpa qui officia deserunt mollit anim id est laborum.</p>
      <p class="paragraph">Lorem ipsum dolor sit amet, consectetur adipisicing elit, sed do eiusmod tempor incididunt ut labore et dolore magna aliqua. Ut enim ad minim veniam, quis nostrud exercitation ullamco laboris nisi ut aliquip ex ea commodo consequat. Duis aute irure dolor in reprehenderit in voluptate velit esse cillum dolore eu fugiat nulla pariatur. Excepteur sint occaecat cupidatat non proident, sunt in culpa qui officia deserunt mollit anim id est laborum.</p>
    </div>
    <p class="closing">Yours Sincerely,</p>
    <div class="signature-area" role="img" aria-label="Handwritten signature"></div>
    <p class="address address--en">42 Harbour Lane, Vernon<br>B.C. Canada V2X 4K7</p>
    <p class="address address--ar">٤٢ هاربر لين، فيرنون<br>كولومبيا البريطانية كندا V2X 4K7</p>
  </article>

  <article class="letterhead letterhead--white">
    <div class="brand"><span class="brand-dot"></span>NORTHWIND COGNITION</div>
    <ul class="contact-list">
      <li><svg class="contact-icon" viewBox="0 0 10 10"><path d="M1 4c0-2 2-3 4-3s4 1 4 3H7V3H3v1zM2 5h6l1 4H1z"/></svg>555.204.7781</li>
      <li><svg class="contact-icon" viewBox="0 0 10 10"><path d="M0 2h10v6H0z M0 2l5 3.5L10 2" stroke="#fff" stroke-width="0.8"/></svg>hello@northwindmail.com</li>
      <li><svg class="contact-icon" viewBox="0 0 10 10"><circle cx="5" cy="5" r="4.6"/><path d="M3 2.5l2 1-1 2 2 1-1 2M7 2l1 2" stroke="#fff" stroke-width="0.7" fill="none"/></svg>www.northwindweb.com</li>
    </ul>
    <div class="letter-body">
      <p class="salutation">Dear customer,</p>
      <p class="paragraph">Lorem ipsum dolor sit amet, consectetur adipisicing elit, sed do eiusmod tempor incididunt ut labore et dolore magna aliqua. Ut enim ad minim veniam, quis nostrud exercitation ullamco laboris nisi ut aliquip ex ea commodo consequat. Duis aute irure dolor in reprehenderit in voluptate velit esse cillum dolore eu fugiat nulla pariatur. Excepteur sint occaecat cupidatat non proident, sunt in culpa qui officia deserunt mollit anim id est laborum.</p>
      <p class="paragraph">Lorem ipsum dolor sit amet, consectetur adipisicing elit, sed do eiusmod tempor incididunt ut labore et dolore magna aliqua. Ut enim ad minim veniam, quis nostrud exercitation ullamco laboris nisi ut aliquip ex ea commodo consequat. Duis aute irure dolor in reprehenderit in voluptate velit esse cillum dolore eu fugiat nulla pariatur. Excepteur sint occaecat cupidatat non proident, sunt in culpa qui officia deserunt mollit anim id est laborum.</p>
      <p class="paragraph">Lorem ipsum dolor sit amet, consectetur adipisicing elit, sed do eiusmod tempor incididunt ut labore et dolore magna aliqua. Ut enim ad minim veniam, quis nostrud exercitation ullamco laboris nisi ut aliquip ex ea commodo consequat. Duis aute irure dolor in reprehenderit in voluptate velit esse cillum dolore eu fugiat nulla pariatur. Excepteur sint occaecat cupidatat non proident, sunt in culpa qui officia deserunt mollit anim id est laborum.</p>
    </div>
    <p class="closing">Yours Sincerely,</p>
    <div class="signature-area" role="img" aria-label="Handwritten signature"></div>
    <p class="address address--en">42 Harbour Lane, Vernon<br>B.C. Canada V2X 4K7</p>
    <p class="address address--ar">٤٢ هاربر لين، فيرنون<br>كولومبيا البريطانية كندا V2X 4K7</p>
  </article>

</div>
</body>
</html>
```